Harbourline construction company Business card design

I need a business card design for my company. I have a logo but dont have business cards with our logo..

www.harbourlineconstructco.com.au

The logo is on the website

I need the same details as this design I have attached. we have changed the logo and colours. just like the website

Industry/Entity Type

Building

```html
<!DOCTYPE html>
<html lang="en">
<head>
<meta charset="utf-8">
<title>Harbourline Construction – Business Cards</title>
<link href="https://fonts.googleapis.com/css2?family=Lato:wght@400;700&family=Cormorant+SC:wght@600&display=swap" rel="stylesheet">
<style>
  :root {
    --bg: #e9e6e1;
    --blue-light: #1cb4e2;
    --blue: #0f94cc;
    --blue-deep: #0a7db8;
    --white: #ffffff;
    --paper: #f7f7f7;
    --grey: #b9bcc0;
    --grey-light: #d6d8da;
    --ink: #1b1b1b;
    --ink-soft: #3a3a3a;
  }
  * { box-sizing: border-box; margin: 0; padding: 0; }
  html, body { width: 1200px; height: 1023px; overflow: hidden; }
  body {
    background: var(--bg);
    font-family: "Lato", Arial, sans-serif;
    position: relative;
  }
  .card {
    position: absolute;
    left: 250px;
    width: 700px;
    height: 400px;
    border-radius: 4px;
    overflow: hidden;
    box-shadow: 0 10px 28px rgba(0,0,0,.22);
  }
  /* Front */
  .card-front {
    top: 80px;
    background: linear-gradient(135deg, var(--blue-light) 0%, var(--blue) 55%, var(--blue-deep) 100%);
    color: var(--white);
    display: flex;
    flex-direction: column;
    align-items: center;
    justify-content: center;
  }
  .front-brand {
    display: flex;
    align-items: center;
    gap: 14px;
    margin-bottom: 34px;
  }
  .brand-square {
    width: 22px; height: 22px;
    background: var(--white);
  }
  .front-brand .brand-name {
    font-size: 40px;
    font-weight: 700;
    letter-spacing: 3px;
    text-transform: uppercase;
    color: var(--white);
  }
  .front-tagline {
    display: flex;
    align-items: center;
    gap: 22px;
  }
  .rule {
    width: 150px;
    height: 2px;
    background: rgba(255,255,255,.85);
  }
  .front-tagline p {
    font-size: 19px;
    line-height: 1.35;
    text-align: center;
  }
  /* Back */
  .card-back {
    top: 543px;
    background: linear-gradient(160deg, var(--white) 0%, var(--paper) 60%, #ececec 100%);
    color: var(--ink);
  }
  .back-brand {
    position: absolute;
    top: 42px;
    left: 48px;
  }
  .back-brand .brand-row {
    display: flex;
    align-items: center;
    gap: 12px;
  }
  .back-brand .brand-square { background: var(--blue); width: 18px; height: 18px; }
  .back-brand .brand-name {
    font-size: 30px;
    font-weight: 700;
    letter-spacing: 2px;
    text-transform: uppercase;
    color: var(--blue);
  }
  .back-brand .brand-rule {
    width: 400px;
    height: 1px;
    background: var(--grey);
    margin: 10px 0 8px;
  }
  .back-brand .tagline {
    font-size: 14px;
    line-height: 1.3;
    color: var(--ink-soft);
  }
  .back-divider {
    position: absolute;
    top: 160px;
    left: 48px;
    width: 604px;
    height: 1px;
    background: var(--grey-light);
  }
  .contacts {
    position: absolute;
    top: 186px;
    left: 48px;
    list-style: none;
  }
  .contacts li {
    display: flex;
    align-items: center;
    gap: 14px;
    font-size: 17px;
    margin-bottom: 12px;
    color: var(--ink);
  }
  .contacts svg { width: 20px; height: 20px; flex: none; }
  .person {
    position: absolute;
    top: 186px;
    right: 56px;
    text-align: right;
  }
  .person-name {
    font-family: "Cormorant SC", Georgia, serif;
    font-weight: 600;
    font-size: 28px;
    letter-spacing: 1px;
    color: var(--ink);
  }
  .person-title {
    font-size: 17px;
    color: var(--blue);
    margin-top: 6px;
  }
  .web-band {
    position: absolute;
    left: 0; right: 0;
    bottom: 22px;
    height: 40px;
    background: linear-gradient(90deg, var(--grey-light), var(--grey));
    display: flex;
    align-items: center;
    padding-left: 48px;
  }
  .web-band span {
    font-size: 16px;
    letter-spacing: .5px;
    color: var(--white);
  }
  .blue-band {
    position: absolute;
    left: 0; right: 0; bottom: 0;
    height: 22px;
    background: linear-gradient(90deg, var(--blue-deep), var(--blue-light));
  }
</style>
</head>
<body>

<section class="card card-front" aria-label="Card front">
  <div class="front-brand">
    <span class="brand-square"></span>
    <span class="brand-name">Harbourline Construction</span>
  </div>
  <div class="front-tagline">
    <span class="rule"></span>
    <p>New Homes, Addition &amp; Renovation<br>Domestic &amp; Commercial Builders</p>
    <span class="rule"></span>
  </div>
</section>

<section class="card card-back" aria-label="Card back">
  <div class="back-brand">
    <div class="brand-row">
      <span class="brand-square"></span>
      <span class="brand-name">Harbourline Construction</span>
    </div>
    <div class="brand-rule"></div>
    <p class="tagline">New Homes, Addition &amp; Renovation<br>Domestic &amp; Commercial Builders</p>
  </div>

  <div class="back-divider"></div>

  <ul class="contacts">
    <li>
      <svg viewBox="0 0 20 20" aria-hidden="true"><rect width="20" height="20" rx="3" fill="#0f94cc"/><path d="M6 5.5c1-.8 1.6-.3 2.2.8.5.9.2 1.3-.4 1.8.6 1.4 1.6 2.4 3 3 .5-.6.9-.9 1.8-.4 1.1.6 1.6 1.2.8 2.2-1 1.2-3 .8-5-1.1S4.8 6.5 6 5.5z" fill="#fff"/></svg>
      <span>9400 2716</span>
    </li>
    <li>
      <svg viewBox="0 0 20 20" aria-hidden="true"><rect x="5.5" y="2" width="9" height="16" rx="1.5" fill="none" stroke="#0f94cc" stroke-width="1.6"/><circle cx="10" cy="15.3" r=".9" fill="#0f94cc"/></svg>
      <span>0400 583 129 (Petra)</span>
    </li>
    <li>
      <svg viewBox="0 0 20 20" aria-hidden="true"><rect x="2" y="4.5" width="16" height="11" rx="1" fill="#0f94cc"/><path d="M2.5 5l7.5 6 7.5-6" fill="none" stroke="#fff" stroke-width="1.3"/></svg>
      <span>info@harbourlineconstructco.com.au</span>
    </li>
  </ul>

  <div class="person">
    <p class="person-name">Petra Lindqvist</p>
    <p class="person-title">Director</p>
  </div>

  <div class="web-band"><span>www.harbourlineconstructco.com.au</span></div>
  <div class="blue-band"></div>
</section>

</body>
</html>
```